Communication and Marketing agency needs a new presentation card

We are a group of communication and marketing agencies specialized in companies that are in the logistics and industrial sector. The head agency is TELVANO Grupo and the group consists of 4 agencies: TELVANO Media, TELVANO Digital, TELVANO Research and EnlazaPorImagen. We hace 4 offices in Spain (Madrid, Barcelona, Valencia and Murcia). We are looking for a clean and attractive design that transmits our experience, brand presence in the market and knowledge to those who receive the card.It has to maintain the colors of the logo that is attached.
Target Market(s)
logistics and industrial sector
Marketing department
Clean and attractive design

```html
<!DOCTYPE html>
<html lang="es">
<head>
<meta charset="utf-8">
<title>TELVANO Grupo – Tarjeta de presentación</title>
<link href="https://fonts.googleapis.com/css2?family=Lato:ital,wght@0,300;0,400;0,700;1,400&display=swap" rel="stylesheet">
<style>
  :root {
    --backdrop: #858585;
    --paper: #ffffff;
    --brand-red: #b01e2a;
    --brand-graphite: #524e4d;
    --ink-light: #ffffff;
    --card-shadow: rgba(0,0,0,0.28);
  }
  * { margin: 0; padding: 0; box-sizing: border-box; }
  html, body { width: 1200px; height: 1200px; overflow: hidden; }
  body {
    background: var(--backdrop);
    font-family: "Lato", Arial, sans-serif;
    position: relative;
  }
  .card {
    position: absolute;
    left: 227px;
    width: 748px;
    height: 485px;
    background: var(--paper);
    box-shadow: 4px 6px 14px var(--card-shadow);
    overflow: hidden;
  }
  .card--front { top: 62px; }
  .card--back { top: 639px; }
  .card svg.shapes { position: absolute; inset: 0; }

  /* Front */
  .front-name {
    position: absolute;
    right: 285px;
    top: 112px;
    text-align: right;
    color: var(--brand-red);
    font-weight: 300;
    line-height: 1;
  }
  .front-name .word { display: block; font-size: 68px; letter-spacing: 4px; }
  .front-name .sub { display: block; font-size: 40px; margin-top: 6px; }
  .front-reflection {
    position: absolute;
    left: 120px;
    top: 236px;
    width: 345px;
    height: 80px;
    background: linear-gradient(to bottom, rgba(176,30,42,0.14), rgba(176,30,42,0));
  }
  .agency-row {
    position: absolute;
    left: 50px;
    top: 424px;
    display: flex;
    gap: 0;
  }
  .agency {
    width: 136px;
    text-align: right;
    color: var(--brand-red);
    font-weight: 400;
    font-size: 13px;
    line-height: 1.15;
  }
  .agency:last-child { text-align: left; padding-left: 18px; }

  /* Back */
  .side-panel {
    position: absolute;
    left: 0; top: 0;
    width: 300px; height: 485px;
    background: var(--brand-graphite);
  }
  .side-name {
    position: absolute;
    right: 17px;
    top: 52px;
    text-align: right;
    color: var(--ink-light);
    font-weight: 300;
    line-height: 1;
  }
  .side-name .word { display: block; font-size: 50px; letter-spacing: 3px; }
  .side-name .sub { display: block; font-size: 30px; margin-top: 6px; }
  .motto {
    position: absolute;
    left: 0; width: 300px;
    top: 441px;
    text-align: center;
    color: var(--ink-light);
    font-size: 9px;
    line-height: 1.3;
  }
  .person-name {
    position: absolute;
    left: 313px;
    top: 250px;
    color: var(--brand-red);
    font-size: 54px;
    font-weight: 400;
    line-height: 1;
    letter-spacing: 0.5px;
  }
  .person-name strong { font-weight: 700; }
  .person-role {
    position: absolute;
    left: 313px;
    top: 313px;
    color: var(--ink-light);
    font-style: italic;
    font-size: 20px;
  }
  .contact {
    position: absolute;
    color: var(--ink-light);
    font-size: 9px;
    line-height: 1.25;
    display: flex;
    align-items: center;
    gap: 12px;
  }
  .contact svg { flex: none; }
  .contact--web { left: 327px; top: 365px; }
  .contact--mail { left: 327px; top: 400px; }
  .contact--phone { left: 327px; top: 440px; }
  .contact--madrid { left: 457px; top: 377px; align-items: flex-start; }
  .contact--barcelona { left: 457px; top: 426px; align-items: flex-start; }
</style>
</head>
<body>

<section class="card card--front" aria-label="Anverso de la tarjeta">
  <svg class="shapes" width="748" height="485" viewBox="0 0 748 485" aria-hidden="true">
    <polygon points="685,25 711,25 578,468 560,468" fill="var(--brand-graphite)"/>
    <polygon points="718,0 748,0 748,485 578,485" fill="var(--brand-red)"/>
  </svg>
  <div class="front-name"><span class="word">TELVANO</span><span class="sub">Grupo</span></div>
  <div class="front-reflection" role="img" aria-label="Reflejo difuminado del nombre del grupo"></div>
  <div class="agency-row">
    <div class="agency">TELVANO<br>Research</div>
    <div class="agency">TELVANO<br>Media</div>
    <div class="agency">TELVANO<br>Digital</div>
    <div class="agency">Enlaza<br>PorImagen</div>
  </div>
</section>

<section class="card card--back" aria-label="Reverso de la tarjeta">
  <div class="side-panel"></div>
  <svg class="shapes" width="748" height="485" viewBox="0 0 748 485" aria-hidden="true">
    <polygon points="300,308 642,308 654,343 300,343" fill="var(--brand-red)"/>
    <polygon points="300,308 636,308 648,343 300,343" fill="var(--brand-graphite)"/>
    <rect x="300" y="344" width="448" height="141" fill="var(--brand-red)"/>
  </svg>
  <div class="side-name"><span class="word">TELVANO</span><span class="sub">Grupo</span></div>
  <p class="motto">“Si haces siempre las cosas de la misma forma,<br>no podrás obtener resultados diferentes.”</p>

  <h1 class="person-name">LUCÍA <strong>SERRANO</strong></h1>
  <p class="person-role">Directora de Estrategia e Investigación</p>

  <div class="contact contact--web">
    <svg width="16" height="16" viewBox="0 0 16 16" aria-hidden="true"><circle cx="8" cy="8" r="6.5" fill="none" stroke="#fff" stroke-width="1.3"/><path d="M1.5 8h13M8 1.5c2.5 2.5 2.5 10.5 0 13M8 1.5c-2.5 2.5-2.5 10.5 0 13" fill="none" stroke="#fff" stroke-width="1"/></svg>
    <span>www.telvano-grupo.es</span>
  </div>
  <div class="contact contact--mail">
    <svg width="16" height="12" viewBox="0 0 16 12" aria-hidden="true"><rect x="0.7" y="0.7" width="14.6" height="10.6" fill="none" stroke="#fff" stroke-width="1.2"/><path d="M0.7 0.7 8 7l7.3-6.3" fill="none" stroke="#fff" stroke-width="1.2"/></svg>
    <span>hola@telvano-grupo.es</span>
  </div>
  <div class="contact contact--phone">
    <svg width="16" height="16" viewBox="0 0 16 16" aria-hidden="true"><path d="M3 1.5l2.5 3-1.4 1.6c.8 2 2.2 3.4 4.3 4.3l1.6-1.4 3 2.5-1.5 2.5C6.5 14 2 9.5 1 3z" fill="#fff"/></svg>
    <span>+34 910 372 418</span>
  </div>
  <div class="contact contact--madrid">
    <svg width="12" height="18" viewBox="0 0 12 18" aria-hidden="true"><path d="M6 0a6 6 0 0 0-6 6c0 4.5 6 12 6 12s6-7.5 6-12a6 6 0 0 0-6-6z" fill="#fff"/><circle cx="6" cy="6" r="2.3" fill="var(--brand-red)"/></svg>
    <span>Calle Río Almanzora, 14.<br>Izquierda, Planta 2ª 28071<br>Madrid</span>
  </div>
  <div class="contact contact--barcelona">
    <svg width="12" height="18" viewBox="0 0 12 18" aria-hidden="true"><path d="M6 0a6 6 0 0 0-6 6c0 4.5 6 12 6 12s6-7.5 6-12a6 6 0 0 0-6-6z" fill="#fff"/><circle cx="6" cy="6" r="2.3" fill="var(--brand-red)"/></svg>
    <span>Carrer de Vilanova, 31.<br>08019 Barcelona</span>
  </div>
</section>

</body>
</html>
```